Web Design Project - Shipping Industry

Goals and Objectives
The objective of the new website is to create a more modern look and feel. The site will also allow for a more effective means of communicating with members while providing the public with information and developments in the local, regional and international shipping industry.
Scope
The website will highlight the history of the organisation inclusive of text and photographs. It will take visitors through the years from beginning to present. Information on the history of the shipping industry will also be included.
It will feature current articles on the organisation, its members and stakeholders in the shipping industry. Member information as well as pertinent details regarding the organisation’s subsidiaries will be documented for the website.
Information as it relates to shipping statistics, case studies, laws and regulations, international treaties and trade documents, shipping terms, careers in shipping, job opportunities, training opportunities, information for shippers including port listing and trade lanes will be main features of the content for the website.
The Association’s community involvement, industry calendar events and related links relevant industry members will also be featured.
Target Market
• The General Public;
• Members of the organization;
• Shipping Industry Stakeholders (local, regional and international);
• Tertiary students conducting research.
• Potential employees
• Potential Business Partners
Best Practice Bench Marketing
The following websites are being looked at:
• Korvel Quays - http://www.korvelquays.example/ (preferred look)
• Tidewell Shipping Association - http://www.twa-ships.example/ (like image transition on main page)
• Brolund - http://www.brolund.example (professional look)
• KHW - http://www.kelharbours.example (preferred color: blue in logo)
• Vendlo - http://www.vendlo.example/electronics/tv-video-audio/ (preferred look for links page: image + short text below + visit site link)
Expected Result
• 3 - 5 pages which must include: [1] main page [2] standard page [3] links page
Target Market(s)
The General Public; Members of the organization; Shipping Industry Stakeholders (local, regional and international); Tertiary students conductin
Industry/Entity Type
Shipping

```html
<!DOCTYPE html>
<html lang="en">
<head>
<meta charset="utf-8">
<title>Meridane PCS</title>
<link rel="stylesheet" href="https://fonts.googleapis.com/css2?family=Cabin:wght@400;500;600&family=Bebas+Neue&family=Arimo:wght@400;700&display=swap">
<style>
:root{
  --ink:#4a4a4a;
  --muted:#6b6b6b;
  --dark:#161718;
  --dark-2:#262829;
  --dark-3:#333536;
  --blue:#1463c4;
  --blue-light:#3a9ad9;
  --blue-deep:#0b4fa8;
  --panel:#f1f0ee;
  --line:#d9dde2;
  --yellow:#f4c21a;
  --white:#ffffff;
}
*{margin:0;padding:0;box-sizing:border-box}
html,body{width:806px;height:1200px;overflow:hidden;background:var(--white)}
body{position:relative;font-family:Arimo,Arial,sans-serif;color:var(--ink)}
.abs{position:absolute}

/* header */
.masthead{left:0;top:0;width:806px;height:120px;background:linear-gradient(#1c1d1e,#0f1011);border-top:4px solid var(--blue)}
.masthead-rule{left:0;top:118px;width:806px;height:3px;background:var(--blue)}
.brand{font-family:Cabin,sans-serif;font-weight:600;font-size:19px;color:var(--white);letter-spacing:.2px}
.brand b{font-weight:600}
.top-logo{left:16px;top:14px}
.top-links{left:258px;top:20px;font-family:Cabin,sans-serif;font-size:11.5px;color:#c9c9c9;word-spacing:1px}
.top-links span{margin:0 6px;color:#888}
.search{left:605px;top:18px;width:183px;height:27px;border-radius:8px;background:var(--dark-3)}
.search svg{position:absolute;right:9px;top:5px}
.ticker{left:0;top:57px;width:806px;height:25px;background:#2c2e2f;color:#e8e8e8;font-size:11px;text-align:center;line-height:25px}

/* hero */
.hero{left:20px;top:87px;width:768px;height:361px;border-radius:8px;overflow:hidden;background:linear-gradient(100deg,#5e6a78 0%,#b78d5e 30%,#d3ab77 55%,#c69a62 75%,#3b4a6a 100%)}
.hero-thumb{left:637px;top:139px;width:132px;height:112px;border:2px solid #e8e8e8;border-radius:4px;background:linear-gradient(#9bb4c8 0%,#b7b1a0 45%,#8a7355 100%)}
.service{left:637px;width:132px;height:34px;border-radius:4px;background:rgba(16,17,18,.92);color:var(--white);font-family:Cabin,sans-serif;font-size:12.5px;letter-spacing:.5px;line-height:34px;padding-left:9px}
.service i{position:absolute;right:9px;top:10px;width:15px;height:15px;border-radius:50%;background:var(--yellow)}
.service i svg{position:absolute;left:3px;top:4px}

/* nav */
.nav{left:20px;top:463px;width:768px;height:42px;border-radius:8px;background:linear-gradient(#2a2c2d,#141516)}
.nav-home{left:20px;top:458px;width:88px;height:52px;border-radius:8px;background:linear-gradient(#2f86dc,#0d52b4);color:var(--white);font-family:Cabin,sans-serif;font-size:14px;text-align:center;line-height:55px}
.nav-item{top:463px;height:42px;line-height:44px;color:var(--white);font-family:Cabin,sans-serif;font-size:14px;letter-spacing:.3px}
.nav-sep{top:468px;width:1px;height:32px;background:#3d3f40}
.social{top:475px;width:21px;height:21px;border-radius:50%;background:radial-gradient(circle at 40% 35%,#9a9a9a,#555)}

/* welcome */
.welcome{left:20px;top:530px;font-family:Cabin,sans-serif;color:#555;font-size:14px;letter-spacing:.3px}
.welcome strong{font-weight:500;color:var(--blue);font-size:22px;letter-spacing:0;margin-left:2px}
.intro{left:27px;top:568px;width:538px;font-size:10.2px;line-height:14.4px;color:var(--muted)}

/* cards */
.card-media{top:660px;width:152px;height:147px;border-radius:8px;background:#ece9e3;padding:8px}
.card-media div{width:100%;height:100%;border-radius:6px}
.card-title{top:815px;font-family:Cabin,sans-serif;font-size:14.5px;color:var(--blue-light)}
.card-text{top:840px;width:146px;font-size:10.2px;line-height:14.4px;color:var(--muted);text-align:justify;hyphens:auto}
.more{font-size:10.2px;color:#333}
.divider{top:660px;width:1px;height:337px;background:var(--line)}

/* banner */
.crates{left:28px;top:1012px;width:116px;height:78px;border-radius:3px;background:linear-gradient(135deg,#d9c7a6,#b89565 50%,#e8eaee 51%,#c9ccd3)}
.banner-text{left:150px;top:1034px;font-family:'Bebas Neue',sans-serif;color:#1d1d1d;font-size:14px;letter-spacing:.2px;white-space:nowrap}
.banner-text strong{font-weight:400;color:var(--blue);font-size:33px;letter-spacing:1px;margin:0 3px;vertical-align:-6px}

/* sidebar */
.side-label{left:600px;top:532px;font-family:Cabin,sans-serif;font-size:12px;color:#444}
.select{left:597px;top:558px;width:168px;height:26px;border-radius:8px;background:linear-gradient(#f4f4f4,#e3e5e8);font-size:9.5px;color:#a8adb3;line-height:26px;padding-left:14px}
.select svg{position:absolute;right:7px;top:9px}
.submit{left:692px;top:594px;width:72px;height:23px;border-radius:5px;background:linear-gradient(#3c8ee0,#1558b6);color:var(--white);font-family:Cabin,sans-serif;font-size:12px;text-align:center;line-height:23px}
.side-head{left:600px;font-family:Cabin,sans-serif;font-size:15px;color:#555}
.side-head svg{vertical-align:-4px;margin-right:4px}
.side-box{left:597px;width:191px;border-radius:8px;background:var(--panel)}
.side-list{list-style:none;position:absolute;left:17px;top:14px;width:170px}
.side-list li{position:relative;font-size:10.2px;line-height:14.2px;color:var(--muted);margin-bottom:6px}
.side-list li::before{content:"";position:absolute;left:-13px;top:4px;width:7px;height:7px;border-radius:50%;background:#a9a9a9}
.side-more{position:absolute;right:16px;font-size:10.2px;color:#333}

/* footer */
.footer{left:0;top:1096px;width:806px;height:104px;background:linear-gradient(#1d1e1f,#111213);border-top:3px solid var(--blue)}
.footer-head{left:21px;top:1108px;font-size:10.5px;color:var(--white);font-weight:700;letter-spacing:.5px}
.footer-col{top:1129px;font-size:10.3px;line-height:14.4px;color:#e6e6e6;letter-spacing:.2px}
.footer-logo{left:651px;top:1129px;font-size:16px;color:#bfbfbf}
.footer-tag{left:651px;top:1152px;font-size:9px;color:#d5d5d5}
.copyright{left:0;top:1180px;width:806px;text-align:center;font-size:9px;color:#bdbdbd}
</style>
</head>
<body>

<header>
  <div class="abs masthead"></div>
  <div class="abs masthead-rule"></div>
  <div class="abs brand top-logo">Meridane PCS</div>
  <nav class="abs top-links">Press Investor<span>|</span>Relations Procurement<span>|</span>Contact Us</nav>
  <div class="abs search">
    <svg width="17" height="17" viewBox="0 0 17 17"><circle cx="6.5" cy="6.5" r="4.8" fill="none" stroke="#fff" stroke-width="2"/><path d="M10 10l5.5 5.5" stroke="#fff" stroke-width="2.6" stroke-linecap="round"/></svg>
  </div>
  <div class="abs ticker">* * * &nbsp;&nbsp;Lorem Ipsum is simply dummy text of the printing and typesetting industry.Lorem Ipsum is simply dummy text ting industry. &nbsp;* * *</div>
</header>

<section>
  <div class="abs hero" role="img" aria-label="Warehouse aisle stacked high with cardboard boxes on pallet racking"></div>
  <div class="abs hero-thumb" role="img" aria-label="Excavator and dump truck at a digging site"></div>
  <div class="abs service" style="top:252px">DIGGING<i><svg width="9" height="7" viewBox="0 0 9 7"><path d="M1 1.5l3.5 3.5 3.5-3.5" fill="none" stroke="#1a1a1a" stroke-width="1.6"/></svg></i></div>
  <div class="abs service" style="top:291px">WELDING<i><svg width="9" height="7" viewBox="0 0 9 7"><path d="M1 5.5l3.5-3.5 3.5 3.5" fill="none" stroke="#1a1a1a" stroke-width="1.6"/></svg></i></div>
  <div class="abs service" style="top:331px">ELECTRICITY<i><svg width="9" height="7" viewBox="0 0 9 7"><path d="M1 5.5l3.5-3.5 3.5 3.5" fill="none" stroke="#1a1a1a" stroke-width="1.6"/></svg></i></div>
</section>

<nav>
  <div class="abs nav"></div>
  <div class="abs nav-home">HOME</div>
  <div class="abs nav-item" style="left:104px">ABOUT US</div>
  <div class="abs nav-sep" style="left:178px"></div>
  <div class="abs nav-item" style="left:192px">SUSTAINABILITY</div>
  <div class="abs nav-sep" style="left:302px"></div>
  <div class="abs nav-item" style="left:315px">NEWS</div>
  <div class="abs nav-sep" style="left:363px"></div>
  <div class="abs nav-item" style="left:378px">CAREERS</div>
  <div class="abs nav-sep" style="left:445px"></div>
  <div class="abs nav-item" style="left:459px">LINKS</div>
  <div class="abs nav-sep" style="left:507px"></div>
  <div class="abs nav-item" style="left:522px">CONTACT US</div>
  <div class="abs social" style="left:683px"></div>
  <div class="abs social" style="left:715px"></div>
  <div class="abs social" style="left:747px"></div>
</nav>

<main>
  <h1 class="abs welcome">WELCOME TO THE <strong>Meridane PCS</strong></h1>
  <p class="abs intro">Lorem Ipsum is simply dummy text of the printing and typesetting industry. Lorem Ipsum has been the industry's standard dummy text ever since the 1500s, when an unknown printer took a galley of type and scrambled it to make a type specimen book. It has survived not only five centuries, but also the leap into electronic typesetting, remaining essentially unchanged. It was popularised in the 1960s with the release of Letterine sheets containing Lorem Ipsum passages, and more recently with desktop publishing software like Alden Typesetter including versions of Lorem Ipsum.</p>

  <div class="abs card-media" style="left:22px"><div role="img" aria-label="Container ship being loaded by port cranes" style="background:linear-gradient(#6fa3d6 0%,#a9c8e6 45%,#b04a3a 62%,#2a3d5e 85%)"></div></div>
  <div class="abs card-media" style="left:223px"><div role="img" aria-label="Stacked colourful shipping containers" style="background:linear-gradient(90deg,#c9452c,#e0782e 30%,#2f7b55 55%,#d9a83a 75%,#6e8ba8)"></div></div>
  <div class="abs card-media" style="left:415px"><div role="img" aria-label="Passenger jet flying above the clouds" style="background:linear-gradient(#3f6fb0 0%,#7aa5d8 55%,#c9d9ec 100%)"></div></div>

  <h2 class="abs card-title" style="left:30px">Lorem Ipsum simply</h2>
  <h2 class="abs card-title" style="left:231px">Lorem Ipsum simply</h2>
  <h2 class="abs card-title" style="left:423px">Lorem Ipsum simply</h2>

  <p class="abs card-text" style="left:27px">Lorem Ipsum is simply dummy text of the printing and typeset&shy;ting industry. Lorem Ipsum has been of Letterine sheets contain&shy;ing Lorem Ipsum passages, and more recently with desktop pub&shy;lishing software like Alden Typesetter including versions of Lorem Ipsum.</p>
  <p class="abs card-text" style="left:229px">Lorem Ipsum is simply dummy text of the printing and typeset&shy;ting industry. Lorem Ipsum has been of Letterine sheets contain&shy;ing Lorem Ipsum passages, and more recently with desktop pub&shy;lishing software like Alden Typesetter including versions of Lorem Ipsum.</p>
  <p class="abs card-text" style="left:421px">Lorem Ipsum is simply dummy text of the printing and typeset&shy;ting industry. Lorem Ipsum has been of Letterine sheets contain&shy;ing Lorem Ipsum passages, and more recently with desktop pub&shy;lishing software like Alden Typesetter including versions of Lorem Ipsum.</p>

  <a class="abs more" style="left:119px;top:975px">View more...</a>
  <a class="abs more" style="left:320px;top:975px">View more...</a>
  <a class="abs more" style="left:512px;top:975px">View more...</a>

  <div class="abs divider" style="left:199px"></div>
  <div class="abs divider" style="left:397px"></div>

  <div class="abs crates" role="img" aria-label="Stacked cardboard cartons on a pallet"></div>
  <div class="abs banner-text">CHECK OUT WHAT'S HAPPENING AT<strong>MERIDANE PCS</strong>AND AROUND US</div>
</main>

<aside>
  <div class="abs side-label">Select a Teminal</div>
  <div class="abs select">Select a Teminal
    <svg width="12" height="8" viewBox="0 0 12 8"><path d="M1.5 1.5l4.5 4.5 4.5-4.5" fill="none" stroke="#1a5fc0" stroke-width="2.2"/></svg>
  </div>
  <div class="abs submit">Submit</div>

  <h3 class="abs side-head" style="top:650px"><svg width="20" height="20" viewBox="0 0 20 20"><circle cx="10" cy="10" r="9" fill="#3c8fd8"/><path d="M4 7c3 0 4 2 6 1s2-4 5-3M5 14c2-2 4 0 6-1s3 2 5 0" fill="none" stroke="#8cc96a" stroke-width="2"/></svg>What's Hot in Town</h3>
  <div class="abs side-box" style="top:678px;height:147px">
    <ul class="side-list">
      <li>Lorem Ipsum is simply dummy text of the printing and typesetting indust.</li>
      <li>Lorem Ipsum is simply dummy text of the printing and typesetting indust.</li>
      <li>Lorem Ipsum is simply dummy text of the printing and typesetting indust.</li>
    </ul>
    <a class="side-more" style="top:121px">View more...</a>
  </div>

  <h3 class="abs side-head" style="top:853px"><svg width="22" height="20" viewBox="0 0 22 20"><rect x="1" y="2" width="13" height="9" rx="2" fill="#2f7fd0"/><path d="M4 11l-1 4 4-4z" fill="#2f7fd0"/><rect x="8" y="7" width="13" height="9" rx="2" fill="#f0a21f"/><path d="M18 16l1 3-4-3z" fill="#f0a21f"/></svg>Association's Meetings</h3>
  <div class="abs side-box" style="top:883px;height:187px">
    <ul class="side-list">
      <li>4.00pm - 6.20pm simply dummy text of the printing and typesetting indust.</li>
      <li>8.30am - 11.30 am dummy text of the printing and typesetting indust.</li>
      <li>Lorem Ipsum is simply dummy text of the printing and typesetting indust.</li>
      <li>8.30am - 11.30 am dummy text of the printing and typesetting indust.</li>
    </ul>
    <a class="side-more" style="top:161px">View more...</a>
  </div>
</aside>

<footer>
  <div class="abs footer"></div>
  <div class="abs footer-head">BUSINESS UNITS</div>
  <div class="abs footer-col" style="left:21px">LOREM TERMINALS<br>LOREM DOMACO<br>DOLPOI SUPERMONST</div>
  <div class="abs footer-col" style="left:168px">LOREM TERMINALS<br>LOREM DOMACO<br>DOLPOI SUPERMONST</div>
  <div class="abs footer-col" style="left:318px">LOREM TERMINALS<br>LOREM DOMACO<br>DOLPOI SUPERMONST</div>
  <div class="abs footer-col" style="left:479px">LOREM TERMINALS<br>LOREM DOMACO<br>DOLPOI SUPERMONST</div>
  <div class="abs brand footer-logo">Meridane PCS</div>
  <div class="abs footer-tag">Loresa tomaple lutus..</div>
  <div class="abs copyright">@2012 . All Rights Reserved</div>
</footer>

</body>
</html>
```